Velmora Grove Club Postcard Design

Need a postcard for this business. Go to velmoragroveclub.com to see the product we are selling. Here's another good postcard you can sample. https://www.rowanpilsbydesign.com/?lightbox=dataItem-qz4tunal
Another one: http://blog.tranquet.com/postcard-examples-from-popular-startups/

```html
<!DOCTYPE html>
<html lang="en">
<head>
<meta charset="utf-8">
<title>Velmora Grove Club Postcard</title>
<link href="https://fonts.googleapis.com/css2?family=Arvo:wght@400;700&family=Varela+Round&display=swap" rel="stylesheet">
<style>
:root{
  --stage:#46464d;
  --teal:#5bb8c1;
  --sage:#a3bb95;
  --orange:#ef6524;
  --green:#6eaa3e;
  --brown:#a0604d;
  --white:#ffffff;
  --ink:#2c2c2c;
  --photo-stick:#a8623a;
  --photo-box:#c9a66b;
}
*{box-sizing:border-box;margin:0;padding:0}
html,body{width:1200px;height:1200px;overflow:hidden;background:var(--stage)}
body{position:relative;font-family:"Varela Round",sans-serif}
.card{position:absolute;overflow:hidden;background:var(--white);box-shadow:0 6px 18px rgba(0,0,0,.35)}
.abs{position:absolute}
.photo{position:absolute}
.brand-title{font-family:"Arvo",serif;font-weight:400;color:var(--white);letter-spacing:1px;white-space:nowrap}
.logo-badge{border-radius:50%;background:var(--white);border:5px solid var(--ink);display:flex;align-items:center;justify-content:center;text-align:center;font-family:"Varela Round",sans-serif;color:var(--ink)}

/* FRONT */
.front{left:57px;top:55px;width:770px;height:512px}
.front .header{left:0;top:0;width:100%;height:71px;background:var(--teal);display:flex;align-items:center;padding-left:30px;gap:14px}
.front .brand-title{font-size:42px}
.paw{width:26px;height:26px;flex:none}
.front .body{left:0;top:71px;width:100%;height:285px;background:var(--sage)}
.front .dogs{left:25px;top:80px;width:270px;height:276px;background:radial-gradient(ellipse at 40% 45%,#4a3b30,#8b7a64 70%,var(--sage));border-radius:40% 40% 0 0}
.front .sticks{left:630px;top:50px;width:85px;height:230px;background:linear-gradient(100deg,transparent 30%,var(--photo-stick) 45%,#c58050 55%,transparent 70%)}
.intro{left:250px;top:100px;width:430px;text-align:center;color:var(--white);font-size:15px;line-height:19px}
.price{left:337px;top:163px;width:222px;height:42px;background:var(--white);border:2px solid #dfe8d8;border-radius:22px;display:flex;align-items:center;justify-content:center;gap:8px}
.price b{color:var(--orange);font-size:28px;font-weight:400}
.price span{color:var(--ink);font-size:16px}
.terms{left:255px;top:222px;width:390px;text-align:center;color:var(--white);font-size:15px;line-height:19px}
.get-tab{left:334px;top:318px;width:228px;height:40px;background:var(--orange);border-radius:22px 22px 0 0;color:var(--white);font-size:21px;text-align:center;padding-top:8px}
.front .logo-badge{left:605px;top:283px;width:145px;height:145px;font-size:17px;line-height:21px;padding:18px;z-index:2}
.strip{left:0;top:356px;width:100%;height:115px;background:var(--white)}
.save{left:18px;top:368px;width:128px;height:128px;border-radius:50%;background:var(--orange);border:4px solid var(--white);color:var(--white);text-align:center;padding-top:18px;line-height:1;z-index:2}
.save .s1{font-size:24px}
.save .s2{font-size:36px;font-weight:700}
.save .s3{font-size:12px;line-height:13px;margin-top:3px}
.perk{top:366px;width:150px;text-align:center;font-size:13px;color:var(--ink);line-height:16px}
.perk .icon{width:60px;height:56px;margin:0 auto 4px;border-radius:8px}
.bottom-bar{left:0;top:471px;width:100%;height:41px;display:flex}
.bar-green{background:var(--green);width:440px;color:var(--white);font-size:15px;display:flex;align-items:center;justify-content:flex-end;padding-right:34px;white-space:nowrap;clip-path:polygon(0 0,100% 0,95% 100%,0 100%)}
.bar-brown{background:var(--brown);flex:1;margin-left:-14px;color:var(--white);font-size:15px;display:flex;align-items:center;padding-left:36px;gap:6px;white-space:nowrap;clip-path:polygon(6% 0,100% 0,100% 100%,0 100%)}

/* BACK */
.back{left:370px;top:630px;width:770px;height:510px;border-top:7px solid var(--green)}
.back .panel-shadow{left:0;top:0;width:100%;height:390px;background:#dde6d6;clip-path:polygon(0 0,60% 0,55% 100%,0 100%)}
.back .panel{left:0;top:0;width:100%;height:390px;background:var(--sage);clip-path:polygon(0 0,57% 0,52% 100%,0 100%)}
.back .logo-badge{left:15px;top:18px;width:90px;height:90px;font-size:11px;line-height:13px;border-width:4px;padding:8px;z-index:2}
.title-band{left:95px;top:38px;width:335px;height:46px;background:var(--teal);display:flex;align-items:center;padding-left:22px;gap:8px}
.title-band .brand-title{font-size:24px}
.title-band .paw{width:18px;height:18px}
.ribbon{left:95px;top:84px;width:330px;height:28px;background:var(--orange);color:var(--white);font-size:14px;display:flex;align-items:center;padding-left:22px;white-space:nowrap;clip-path:polygon(0 0,100% 0,96% 100%,0 100%)}
.checklist{left:38px;top:140px;list-style:none;color:var(--white);font-size:15px;line-height:23px}
.checklist li{display:flex;gap:8px;align-items:flex-start;white-space:nowrap}
.checklist li.indent{padding-left:26px}
.checklist svg{width:18px;height:18px;margin-top:3px;flex:none}
.stamp{left:630px;top:28px;width:105px;height:110px;border:2px solid #888}
.back .dogs{left:420px;top:220px;width:350px;height:270px;background:radial-gradient(ellipse at 35% 55%,#3b2c22,#6e5a45 45%,#d7b27a 70%,transparent 80%)}
.url-tab{left:470px;top:440px;width:300px;height:40px;background:var(--teal);border-radius:20px 0 0 0;color:var(--white);font-size:16px;display:flex;align-items:center;padding-left:40px}
.testimonial{left:0;top:390px;width:440px;height:100px;background:var(--white)}
.testimonial .paw-photo{left:40px;top:12px;width:90px;height:80px;border-radius:45%;background:radial-gradient(circle at 50% 60%,#9a7a5a,#cfcfcf 65%)}
.testimonial h3{left:140px;top:8px;color:var(--orange);font-size:17px;font-weight:400}
.testimonial p{left:140px;top:32px;width:290px;font-size:10.5px;line-height:13px;color:var(--ink)}
.back .foot{left:0;top:490px;width:100%;height:13px;background:var(--green)}
</style>
</head>
<body>

<section class="card front">
  <div class="abs header">
    <svg class="paw" viewBox="0 0 26 26" aria-hidden="true"><g fill="#fff"><ellipse cx="13" cy="17" rx="6.5" ry="5.5"/><circle cx="5" cy="10" r="2.8"/><circle cx="10" cy="5" r="2.8"/><circle cx="16" cy="5" r="2.8"/><circle cx="21" cy="10" r="2.8"/></g></svg>
    <h1 class="brand-title">VELMORA GROVE CLUB</h1>
    <svg class="paw" viewBox="0 0 26 26" aria-hidden="true"><g fill="#fff"><ellipse cx="13" cy="17" rx="6.5" ry="5.5"/><circle cx="5" cy="10" r="2.8"/><circle cx="10" cy="5" r="2.8"/><circle cx="16" cy="5" r="2.8"/><circle cx="21" cy="10" r="2.8"/></g></svg>
  </div>
  <div class="abs body"></div>
  <div class="photo dogs" role="img" aria-label="Photo of a tri-colour mountain dog and a pug wearing large pink sunglasses"></div>
  <div class="photo sticks" role="img" aria-label="Photo of long bully chew sticks"></div>
  <p class="abs intro">VELMORA GROVE CLUB is a monthly subscription club that offers the most popular dog treats at intervals that fit your dog's chewing appetite.</p>
  <div class="abs price"><b>$12.95</b><span>a month!</span></div>
  <p class="abs terms">You will be charged monthly.<br>You can cancel anytime.<br>No muss, no fuss, no disappointed pups.</p>
  <div class="abs get-tab">You'll Get:</div>
  <div class="abs strip"></div>
  <div class="abs logo-badge">Velmora Grove Club</div>
  <div class="abs perk" style="left:200px"><div class="icon" role="img" aria-label="Illustration of a happy cartoon puppy with a seal" style="background:#e8ddd2"></div>Doggy Joy<br>GUARANTEE!</div>
  <div class="abs perk" style="left:330px"><div class="icon" role="img" aria-label="Silhouette of a cow marked premium quality" style="background:#222"></div>Sourced From<br>Free Range Cattle</div>
  <div class="abs perk" style="left:465px"><div class="icon" role="img" aria-label="Illustration of a cardboard shipping box" style="background:var(--photo-box)"></div>Shipped to<br>Your Doorstep!</div>
  <div class="abs bottom-bar">
    <div class="bar-green">By Sign Up for Subscription.</div>
    <div class="bar-brown">Learn More:
      <svg width="16" height="16" viewBox="0 0 16 16" aria-hidden="true"><g fill="none" stroke="#fff" stroke-width="1.3"><circle cx="8" cy="8" r="6.5"/><ellipse cx="8" cy="8" rx="3" ry="6.5"/><path d="M1.5 8h13"/></g></svg>
      www.velmoragroveclub.com</div>
  </div>
  <div class="abs save"><div class="s1">SAVE</div><div class="s2">50%</div><div class="s3">on your<br>first month</div></div>
</section>

<section class="card back">
  <div class="abs panel-shadow"></div>
  <div class="abs panel"></div>
  <div class="abs title-band">
    <h2 class="brand-title">VELMORA GROVE CLUB</h2>
    <svg class="paw" viewBox="0 0 26 26" aria-hidden="true"><g fill="#fff"><ellipse cx="13" cy="17" rx="6.5" ry="5.5"/><circle cx="5" cy="10" r="2.8"/><circle cx="10" cy="5" r="2.8"/><circle cx="16" cy="5" r="2.8"/><circle cx="21" cy="10" r="2.8"/></g></svg>
  </div>
  <div class="abs ribbon">TOP QUALITY &amp; HEALTHY BULL STICKS</div>
  <div class="abs logo-badge">Velmora Grove Club</div>
  <div class="abs stamp"></div>
  <ul class="abs checklist">
    <li><svg viewBox="0 0 18 18"><circle cx="8" cy="10" r="6.5" fill="none" stroke="#ef6524" stroke-width="2"/><path d="M4.5 9.5l3 3L16 3" fill="none" stroke="#ef6524" stroke-width="2.2"/></svg>USDA Certified, Inspected &amp; Approved</li>
    <li><svg viewBox="0 0 18 18"><circle cx="8" cy="10" r="6.5" fill="none" stroke="#ef6524" stroke-width="2"/><path d="M4.5 9.5l3 3L16 3" fill="none" stroke="#ef6524" stroke-width="2.2"/></svg>100% Digestible Safely Passes through your dog</li>
    <li><svg viewBox="0 0 18 18"><circle cx="8" cy="10" r="6.5" fill="none" stroke="#ef6524" stroke-width="2"/><path d="M4.5 9.5l3 3L16 3" fill="none" stroke="#ef6524" stroke-width="2.2"/></svg>Slowly oven baked 100% Natural beef pizzle.</li>
    <li><svg viewBox="0 0 18 18"><circle cx="8" cy="10" r="6.5" fill="none" stroke="#ef6524" stroke-width="2"/><path d="M4.5 9.5l3 3L16 3" fill="none" stroke="#ef6524" stroke-width="2.2"/></svg>No chemicals used</li>
    <li><svg viewBox="0 0 18 18"><circle cx="8" cy="10" r="6.5" fill="none" stroke="#ef6524" stroke-width="2"/><path d="M4.5 9.5l3 3L16 3" fill="none" stroke="#ef6524" stroke-width="2.2"/></svg>Dissolves into safe, soft form.</li>
    <li><svg viewBox="0 0 18 18"><circle cx="8" cy="10" r="6.5" fill="none" stroke="#ef6524" stroke-width="2"/><path d="M4.5 9.5l3 3L16 3" fill="none" stroke="#ef6524" stroke-width="2.2"/></svg>Naturally Contains glucosamine &amp; chondroitin</li>
    <li class="indent">for joint support</li>
    <li><svg viewBox="0 0 18 18"><circle cx="8" cy="10" r="6.5" fill="none" stroke="#ef6524" stroke-width="2"/><path d="M4.5 9.5l3 3L16 3" fill="none" stroke="#ef6524" stroke-width="2.2"/></svg>Promotes Oral Health</li>
    <li><svg viewBox="0 0 18 18"><circle cx="8" cy="10" r="6.5" fill="none" stroke="#ef6524" stroke-width="2"/><path d="M4.5 9.5l3 3L16 3" fill="none" stroke="#ef6524" stroke-width="2.2"/></svg>Provides Stress Relief</li>
    <li><svg viewBox="0 0 18 18"><circle cx="8" cy="10" r="6.5" fill="none" stroke="#ef6524" stroke-width="2"/><path d="M4.5 9.5l3 3L16 3" fill="none" stroke="#ef6524" stroke-width="2.2"/></svg>High in Protein, Low in Fat</li>
  </ul>
  <div class="photo dogs" role="img" aria-label="Photo of a chocolate labrador licking its nose beside a golden retriever, with bully sticks"></div>
  <div class="abs url-tab">www.velmoragroveclub.com</div>
  <div class="abs testimonial">
    <div class="abs paw-photo" role="img" aria-label="Paw-shaped frame holding a small photo of a customer's dog"></div>
    <h3 class="abs">Slowly but surely</h3>
    <p class="abs">My little hazel is 20 pounds but has the appetite of a much bigger dog. I'm always worried that she eats her food way too fast. A friend suggested bully sticks and i found this club. The cool thing about the bully sticks is that she takes her sweet time. ~Marisol T.</p>
  </div>
  <div class="abs foot"></div>
</section>

</body>
</html>
```